Consulting Firm stationery design

Now that the MakerHive has given us a new logo we'll now need to have all our stationery designed. So we're asking for this community to help us once again.We're looking to get from you Letterheads (Header and Footer, suitable to be applied on a .docx format. Vectors are required but keep this in mind), Envelopes (Front and Back designs, back is not a must but desirable depending on your design), 9"x 12" Pocket Folders (consider design for front and back, also for pockets as well), Business Cards.An elegant design is a must have, mostly for Folders and Envelopes. The idea with this two is to stand out from others when they're handed over. Ideas are welcomed, we were thinking maybe on some texturing simulation for these.Folders will have 3 addresses and contact information. Envelopes will have 1 address and contact information.Brand Manual attached. vendaluxo logo has been copyrighted already. I'm also attaching the current stationary designs (these never got to be out for production but was going to be before we made the brand changes); Pocker folders page 1 to 4 (pages 2 and 4 are the pocket designs), Pages 5 and 6 (6 is the back of the envelope), Pages 7 and 8 (8 is the back of the business card). No letterhead within these designs as it just had the logo and address.

Industry/Entity Type

Business Consultant

Font styles to use
Serif
Sans Serif

Requirements
Must have
• Elegance
Nice to have
• Modern looking out of common

```html
<!DOCTYPE html>
<html lang="en">
<head>
<meta charset="utf-8">
<title>vendaluxo business cards</title>
<link rel="stylesheet" href="https://fonts.googleapis.com/css2?family=Open+Sans:wght@400;600;700&display=swap">
<style>
  :root{
    --stage:#2b2d31;
    --card-dark:#3b3c41;
    --card-white:#ffffff;
    --brand-blue:#1a7bc9;
    --brand-blue-deep:#0f5fa8;
    --logo-grey:#e9e9e9;
    --text-grey:#6f7176;
    --map-dark:#45464c;
    --map-light:#ececec;
    --hatch:#cfd0d3;
  }
  *{box-sizing:border-box;margin:0;padding:0}
  html,body{width:1200px;height:900px;overflow:hidden}
  body{background:var(--stage);font-family:"Open Sans",Arial,sans-serif;position:relative}

  .card{position:absolute;border-radius:26px;overflow:hidden;box-shadow:0 14px 30px rgba(0,0,0,.35)}

  /* portrait contact card */
  .card--contact{left:110px;top:150px;width:340px;height:595px;background:var(--card-white)}
  .contact-top{position:absolute;left:0;top:0;width:100%;height:265px;background:var(--card-dark)}
  .contact-band{position:absolute;left:0;top:265px;width:100%;height:26px;display:flex}
  .contact-band .band-blue{width:22%;background:var(--brand-blue)}
  .contact-band .band-hatch{flex:1;background:repeating-linear-gradient(135deg,var(--hatch) 0 2px,#fff 2px 6px)}
  .contact-map{position:absolute;left:60px;top:330px;width:230px;height:170px;border-radius:40px;background:radial-gradient(ellipse at center,var(--map-light) 40%,rgba(236,236,236,0) 72%)}
  .contact-body{position:absolute;left:36px;top:318px;right:30px}
  .person-name{color:var(--brand-blue);font-weight:700;font-size:22px;line-height:1.1}
  .person-role{color:var(--text-grey);font-size:13px;margin-top:4px}
  .name-rule{height:2px;width:170px;margin-top:8px;background:linear-gradient(90deg,var(--brand-blue),rgba(26,123,201,0))}
  .contact-list{list-style:none;margin-top:28px}
  .contact-list li{display:flex;align-items:flex-start;gap:9px;font-size:12.5px;color:var(--text-grey);margin-bottom:10px;line-height:1.45}
  .contact-list li.address{color:var(--brand-blue);font-weight:700;font-size:13px;margin-bottom:14px}
  .contact-list svg{flex:none;width:12px;height:12px;margin-top:3px}

  /* logo lockup */
  .logo{position:absolute;display:flex;align-items:center;gap:12px;font-weight:700;color:var(--brand-blue);letter-spacing:-1px}
  .logo .logo-dot{border-radius:50%;background:var(--logo-grey)}
  .card--contact .logo{left:50%;top:132px;transform:translate(-50%,-50%);font-size:46px}
  .card--contact .logo-dot{width:14px;height:14px}

  /* landscape brand card */
  .card--brand{left:510px;top:290px;width:595px;height:340px;background:var(--card-dark)}
  .brand-map{position:absolute;left:90px;top:20px;width:420px;height:260px;border-radius:80px;background:radial-gradient(ellipse at center,var(--map-dark) 45%,rgba(69,70,76,0) 72%)}
  .card--brand .logo{left:50%;top:128px;transform:translate(-50%,-50%);font-size:64px}
  .card--brand .logo-dot{width:18px;height:18px}
  .brand-band{position:absolute;left:0;top:232px;width:100%;height:36px;display:flex}
  .brand-band .band-blue{width:22%;background:linear-gradient(90deg,var(--brand-blue-deep),var(--brand-blue))}
  .brand-band .band-blue:last-child{width:30%;background:linear-gradient(90deg,var(--brand-blue),var(--brand-blue-deep))}
  .brand-band .band-hatch{flex:1;background:repeating-linear-gradient(135deg,var(--hatch) 0 2px,#fff 2px 6px)}
  .brand-url{position:absolute;left:0;right:0;top:276px;text-align:center;color:#fff;font-weight:700;font-size:19px;letter-spacing:.3px}
</style>
</head>
<body>

<section class="card card--contact" aria-label="Business card, contact side">
  <div class="contact-top">
    <div class="logo"><span class="logo-name">vendaluxo</span><span class="logo-dot"></span></div>
  </div>
  <div class="contact-band"><span class="band-blue"></span><span class="band-hatch"></span></div>
  <div class="contact-map" role="img" aria-label="Faint dotted world map"></div>
  <div class="contact-body">
    <p class="person-name">Marco Delgado</p>
    <p class="person-role">Co-Founder</p>
    <div class="name-rule"></div>
    <ul class="contact-list">
      <li class="address">
        <svg viewBox="0 0 12 12"><circle cx="6" cy="6" r="5.5" fill="#6f7176"/><path d="M6 2.6a2 2 0 0 0-2 2c0 1.6 2 4 2 4s2-2.4 2-4a2 2 0 0 0-2-2z" fill="#fff"/></svg>
        <span>418 Harbor View Lane, Suite C4<br>Dover, Delaware 19901 US</span>
      </li>
      <li>
        <svg viewBox="0 0 12 12"><circle cx="6" cy="6" r="5.5" fill="#6f7176"/><path d="M4 3.2l1 1.4-.6.7c.4.9 1 1.5 1.9 1.9l.7-.6 1.4 1-.6 1c-2.4-.2-4.2-2-4.4-4.4z" fill="#fff"/></svg>
        <span>+1 (829) 555-0147</span>
      </li>
      <li>
        <svg viewBox="0 0 12 12"><circle cx="6" cy="6" r="5.5" fill="#6f7176"/><rect x="3" y="4" width="6" height="4.2" fill="#fff"/><path d="M3 4l3 2.3L9 4" stroke="#6f7176" stroke-width=".7" fill="none"/></svg>
        <span>info@vendaluxo.do</span>
      </li>
      <li>
        <svg viewBox="0 0 12 12"><circle cx="6" cy="6" r="5.5" fill="#6f7176"/><circle cx="6" cy="6" r="3" fill="none" stroke="#fff" stroke-width=".8"/><path d="M3 6h6M6 3v6" stroke="#fff" stroke-width=".7"/></svg>
        <span>www.vendaluxo.do</span>
      </li>
    </ul>
  </div>
</section>

<section class="card card--brand" aria-label="Business card, brand side">
  <div class="brand-map" role="img" aria-label="Faint dotted world map"></div>
  <div class="logo"><span class="logo-name">vendaluxo</span><span class="logo-dot"></span></div>
  <div class="brand-band"><span class="band-blue"></span><span class="band-hatch"></span><span class="band-blue"></span></div>
  <p class="brand-url">www.vendaluxo.do</p>
</section>

</body>
</html>
```